Dental Office Business Card

We need a business card for our pediatric dentistry office.
On one side the design needs to contain the following:
our logo (attached)
Corvin Kids Dental Studio
Tamsin Vetrakovich, DDS
Board Certified Pediatric Dentist
Tel: (617) 555-0148)
Fax: (617) 555-0193
Email: info@corvinkidsdental.example
Web: www.corvinkidsdental.example
Address: 42 Brambury Ln, Suite 208, Marrowfield, ST 00000

On the other side of the card, the design needs to have an appointment reminder (date and time as well as day of the week) similar to the design attached (no need for appointment reason “For”)

```html
<!DOCTYPE html>
<html lang="en">
<head>
<meta charset="utf-8">
<title>Corvin Kids Dental Studio – Business Card</title>
<link href="https://fonts.googleapis.com/css2?family=Montserrat:wght@400;500;600;700&display=swap" rel="stylesheet">
<style>
  :root{
    --stage:#2b2b2b;
    --card-white:#ffffff;
    --card-black:#1f1f1f;
    --green:#7fc58e;
    --green-line:#86c996;
    --ink:#1c1c1c;
    --white:#ffffff;
  }
  *{box-sizing:border-box;margin:0;padding:0}
  html,body{width:1200px;height:875px;overflow:hidden;background:var(--stage);
    font-family:"Montserrat",sans-serif}
  .canvas{width:1200px;height:875px;display:flex;flex-direction:column;
    align-items:center;justify-content:center;gap:40px}
  .card{width:640px;height:366px;border-radius:20px;position:relative;overflow:hidden;
    box-shadow:0 14px 30px rgba(0,0,0,.45)}

  /* appointment side */
  .appointment{background:var(--card-white);color:var(--ink);padding:40px 46px;
    display:flex;flex-direction:column;justify-content:space-between}
  .appointment__title{color:var(--green);font-weight:700;font-size:23px;letter-spacing:.5px;
    text-align:center}
  .field{display:flex;align-items:flex-end;gap:10px;font-size:15px;font-weight:500;
    text-transform:uppercase}
  .field__line{flex:1;border-bottom:1.5px solid var(--green-line);height:18px}
  .field__label{white-space:nowrap}
  .weekday__label{font-weight:700;font-size:17px;text-transform:uppercase;margin-bottom:14px}
  .weekday__list{display:flex;justify-content:space-between;list-style:none}
  .weekday__item{display:flex;align-items:center;gap:7px;font-size:13px;font-weight:500}
  .checkbox{width:18px;height:18px;border:1.5px solid var(--green-line)}
  .appointment__note{font-size:14px;text-align:center;line-height:1.45}

  /* contact side */
  .contact{background:var(--card-black);color:var(--white);display:flex;align-items:center;
    padding:0 40px}
  .brand{width:250px;display:flex;align-items:center;gap:12px}
  .brand__dot{width:26px;height:26px;border-radius:50%;background:var(--green);flex:none}
  .brand__name{font-weight:600;font-size:25px;line-height:1.15;color:var(--white)}
  .divider{width:2px;height:180px;background:var(--green);margin:0 26px 0 18px}
  .details{flex:1}
  .details__name{color:var(--green);font-weight:700;font-size:20px}
  .details__role{font-size:13.5px;font-weight:500;margin:3px 0 16px}
  .details__address{font-size:13px;line-height:1.4;margin-bottom:12px}
  .details__list{list-style:none;font-size:13px;line-height:1.55}
  .details__item{display:flex;align-items:center;gap:9px}
  .icon{width:12px;height:12px;flex:none}
</style>
</head>
<body>
<main class="canvas">

  <section class="card appointment" aria-label="Appointment reminder side">
    <h2 class="appointment__title">YOUR NEXT APPOINTMENT</h2>
    <div class="field"><span class="field__label">Name</span><span class="field__line"></span></div>
    <div class="field">
      <span class="field__label">Date</span><span class="field__line"></span>
      <span class="field__label">Time</span><span class="field__line"></span>
      <span class="field__label">AM/PM</span>
    </div>
    <div class="weekday">
      <p class="weekday__label">Day of the week</p>
      <ul class="weekday__list">
        <li class="weekday__item"><span class="checkbox"></span>MON</li>
        <li class="weekday__item"><span class="checkbox"></span>TUE</li>
        <li class="weekday__item"><span class="checkbox"></span>WED</li>
        <li class="weekday__item"><span class="checkbox"></span>THU</li>
        <li class="weekday__item"><span class="checkbox"></span>FRI</li>
        <li class="weekday__item"><span class="checkbox"></span>SAT</li>
        <li class="weekday__item"><span class="checkbox"></span>SUN</li>
      </ul>
    </div>
    <p class="appointment__note">If you are unable to keep your appointment, please call reschedule/<br>cancel 48 hours prior to your appointment</p>
  </section>

  <section class="card contact" aria-label="Contact side">
    <div class="brand">
      <span class="brand__dot"></span>
      <span class="brand__name">Corvin Kids<br>Dental Studio</span>
    </div>
    <span class="divider"></span>
    <div class="details">
      <h1 class="details__name">Tamsin Vetrakovich, DDS</h1>
      <p class="details__role">Board Certified Pediatric Dentist</p>
      <p class="details__address">42 Brambury Ln, Suite<br>208, Marrowfield, ST 00000</p>
      <ul class="details__list">
        <li class="details__item">
          <svg class="icon" viewBox="0 0 12 12"><rect x="3" y="0.5" width="6" height="11" rx="1" fill="none" stroke="#fff"/></svg>
          (617) 555-0148)</li>
        <li class="details__item">
          <svg class="icon" viewBox="0 0 12 12"><rect x="3" y="0" width="6" height="4" fill="#fff"/><rect x="0" y="4" width="12" height="5" fill="#fff"/><rect x="3" y="8" width="6" height="4" fill="#fff" stroke="#1f1f1f"/></svg>
          (617) 555-0193</li>
        <li class="details__item">
          <svg class="icon" viewBox="0 0 12 12"><rect x="0" y="2" width="12" height="8" fill="#fff"/><path d="M0 2 L6 7 L12 2" fill="none" stroke="#1f1f1f"/></svg>
          info@corvinkidsdental.example</li>
        <li class="details__item">
          <svg class="icon" viewBox="0 0 12 12"><circle cx="6" cy="6" r="5.5" fill="#fff"/><ellipse cx="6" cy="6" rx="2.3" ry="5.5" fill="none" stroke="#1f1f1f"/><line x1="0.5" y1="6" x2="11.5" y2="6" stroke="#1f1f1f"/></svg>
          www.corvinkidsdental.example</li>
      </ul>
    </div>
  </section>

</main>
</body>
</html>
```